Redesign of existing template to align with brand identify

We need page template redesign for our teach English abroad content cluster. Our dev guy created a mockup for a page template, although decent, it needs a designer's touch to elevate it and make sure it aligns with our existing brand identity on the website. The mockup has been created on figma and we would prefer the design files to include figma files.

The designer can either work from scratch or they work on the design we already have on the figma link - https://www.drafmoly-board.net/file/Q7wRpK2mTzVxa9bLcNe4Hd/Teach-English-Abroad-Mockup?node-id=41%3A19&t=pa4uKmWzrTqsYvBn-7

We need a design for both desktop and mobile layout. You can visit our website here https://www.brinvoldlearning.com/ to see our brand colors and style. We want to use a lot of white space on the design with a hint of our brand colors.

Video 1 - https://clipvarno.net/502746318/4d7e1a9c3f >> watch this one first
Video 2 - https://clipvarno.net/502748027/e6a2f05d71

```html
<!DOCTYPE html>
<html lang="en">
<head>
<meta charset="utf-8">
<meta name="viewport" content="width=device-width, initial-scale=1">
<title>Teach English In South Korea – Brinvold Learning</title>
<link href="https://fonts.googleapis.com/css2?family=Poppins:wght@400;500;600;700;800&family=Montserrat:wght@800&family=Dancing+Script:wght@600&display=swap" rel="stylesheet">
<style>
:root{
  --teal:#14b9c1;
  --navy:#1d3649;
  --ink:#1f1f1f;
  --body:#5d5d5d;
  --muted:#8a8a8a;
  --line:#ececec;
  --soft:#f4f4f4;
  --white:#fff;
  --wrap:980px;
}
*{box-sizing:border-box;margin:0;padding:0}
html,body{width:1200px;height:4468px;overflow:hidden}
body{font-family:'Poppins',sans-serif;color:var(--ink);background:var(--white)}
a{color:inherit;text-decoration:none}
ul{list-style:none}
.wrap{width:var(--wrap);margin:0 auto;position:relative}
.btn{display:inline-flex;align-items:center;justify-content:center;background:var(--teal);color:#fff;font-weight:600;font-size:14px;width:140px;height:34px;flex:none}

/* header */
.site-header{height:78px;border-bottom:1px solid var(--line)}
.site-header .wrap{height:100%;display:flex;justify-content:space-between;align-items:flex-start}
.brand{margin-top:20px;display:flex;align-items:center;gap:8px;font-weight:700;font-size:19px;color:var(--teal)}
.brand-mark{width:22px;height:22px;background:var(--teal);border-radius:3px}
.header-right{display:flex;flex-direction:column;align-items:flex-end;padding-top:16px}
.search{display:flex;gap:8px}
.search-field{width:120px;height:19px;border:1px solid #333;font-size:7px;padding:4px 5px;color:#666;display:flex;justify-content:space-between}
.search-btn{height:19px;padding:0 12px;background:var(--teal);color:#fff;font-size:7px;font-weight:600;display:flex;align-items:center}
.main-nav{margin-top:12px;display:flex;gap:40px;font-size:15px;color:#333}
.main-nav .current{color:var(--teal)}

/* hero */
.hero{height:500px;background:linear-gradient(180deg,#7f92a6 0%,#5d6f6e 35%,#4e6a3a 60%,#3e5a28 100%);
  color:#fff;text-align:center;padding-top:170px}
.hero-script{font-family:'Dancing Script',cursive;font-size:38px;line-height:50px}
.hero-title{margin-top:12px;font-size:53px;line-height:66px;font-weight:700}
.crumbs{margin-top:12px;font-size:14px;font-weight:600;display:flex;justify-content:center;gap:16px}
.crumbs .current{color:var(--teal)}

/* intro */
.intro{height:745px;padding-top:16px}
.meta-row{height:40px;display:flex;justify-content:space-between;align-items:center;padding-left:2px}
.updated{font-size:13px;color:var(--muted);display:flex;align-items:center;gap:6px}
.share{display:flex;gap:4px}
.share span{width:31px;height:31px;border-radius:50%}
.intro-grid{margin-top:47px;display:grid;grid-template-columns:270px 654px;column-gap:56px}
.toc{padding-top:5px}
.toc-group{font-size:19px;font-weight:500;display:flex;align-items:center;gap:14px;color:#222;height:24px}
.toc-group svg{flex:none}
.toc-sub{margin:14px 0 26px}
.toc-sub li{font-size:15px;color:#333;height:30px;display:flex;align-items:center;gap:12px}
.toc-sub li::before{content:"";border-left:5px solid #333;border-top:4px solid transparent;border-bottom:4px solid transparent}
.toc-sub li.active{color:var(--teal)}
.toc-sub li.active::before{border-left-color:var(--teal)}
.toc-group.spaced{height:60px}
.article h2{font-size:25px;font-weight:700;color:var(--teal);margin-bottom:18px;line-height:36px}
.article p{font-size:14.5px;line-height:26px;color:var(--body);text-align:justify;margin-bottom:26px}
.checks{margin:-4px 0 26px}
.checks li{display:flex;align-items:center;gap:14px;font-size:14.5px;color:var(--body);height:34px}

/* call to action */
.cta{height:415px;background:var(--navy);color:#fff}
.cta .wrap{width:1000px;height:100%;display:flex;align-items:center;justify-content:space-between}
.cta-copy{width:470px;padding-top:8px}
.cta h2{font-size:40px;font-weight:700;line-height:50px}
.cta p{margin-top:16px;font-size:14px;line-height:26px}
.cta .btn{margin-top:30px;margin-left:5px}
.cta-art{width:480px;height:300px;border-radius:6px;
  background:linear-gradient(115deg,#28495f 0%,#2e8f99 40%,#c9b28a 62%,#eef0f2 80%,#dfe3e6 100%)}

/* shared section heading */
.sec-head{display:flex;justify-content:space-between;align-items:center;height:50px}
.sec-head h2{font-size:38px;font-weight:700}

/* jobs */
.jobs{height:606px;padding-top:88px}
.job-grid{margin-top:23px;display:grid;grid-template-columns:repeat(3,310px);gap:26px 25px;padding-left:2px}
.job{height:158px;background:#fff;box-shadow:0 4px 18px rgba(0,0,0,.07);padding:24px 26px;position:relative}
.job h3{font-size:17px;font-weight:700;line-height:28px;width:200px}
.job .badge{position:absolute;top:24px;right:22px;width:38px;height:38px;border-radius:50%;box-shadow:0 2px 8px rgba(0,0,0,.12);display:flex;align-items:center;justify-content:center;font-size:13px;font-weight:600;color:var(--navy)}
.tags{display:flex;gap:14px;font-size:9.5px;margin-top:14px}
.tags span:first-child{color:var(--teal)}
.job-foot{display:flex;justify-content:space-between;font-size:10.5px;color:#555;margin-top:12px}
.job-foot a{color:var(--teal);text-decoration:underline}

/* places */
.places{height:561px;background:var(--soft);padding-top:100px;position:relative}
.place-row{margin-top:26px;display:grid;grid-template-columns:repeat(4,235px);gap:13px;padding-left:2px}
.place{height:282px;position:relative}
.place span{position:absolute;bottom:14px;left:0;width:100%;text-align:center;color:#fff;font-size:22px;font-weight:700}
.arrow{position:absolute;top:312px;width:40px;height:40px;border-radius:50%;background:#fff;border:1px solid #ddd;display:flex;align-items:center;justify-content:center}
.arrow.prev{left:36px}
.arrow.next{left:1124px}

/* related posts */
.posts{height:924px;padding-top:97px}
.post-grid{margin-top:22px;display:grid;grid-template-columns:repeat(3,310px);gap:46px 25px;padding-left:2px}
.post{height:296px}
.post-img{height:195px}
.post-body{position:relative;margin:-28px 16px 0;background:#fff;padding:8px 16px 0}
.post-cat{font-size:18px;color:#666;line-height:26px}
.post h3{font-family:'Montserrat',sans-serif;font-weight:800;font-size:21px;line-height:27px;margin-top:6px;color:#222}
.post-meta{display:flex;justify-content:space-between;font-size:12px;color:#777;margin-top:18px;white-space:nowrap}
.post-meta span{display:flex;align-items:center;gap:5px}

/* footer */
.footer{height:419px;background:var(--teal);color:#fff;padding-top:52px}
.footer-brand{display:flex;justify-content:center;align-items:center;gap:10px;font-size:24px;font-weight:700;height:60px}
.footer-brand i{width:26px;height:26px;background:#fff;display:block;border-radius:3px}
.footer-cols{width:660px;margin:43px auto 0;display:flex;justify-content:space-between;text-align:center}
.footer-col{width:110px}
.footer-col h4{font-size:11px;font-weight:700;margin-bottom:10px;line-height:13px}
.footer-col li{font-size:8.5px;line-height:11px;margin:0 auto 12px;max-width:100px}
.footer-base{height:165px;position:relative;background:linear-gradient(180deg,#1f4e52 0%,#16313a 50%,#0f2129 100%);color:#fff;text-align:center}
.call{position:absolute;top:60px;width:100%;font-size:10px;font-weight:600}
.address{position:absolute;top:107px;width:100%;font-size:8px}
.legal{position:absolute;top:135px;width:100%;font-size:8px}
.cards{position:absolute;top:97px;left:18px;display:flex;gap:20px}
.cards span{width:34px;height:20px;background:#fff;border-radius:3px;color:#333;font-size:7px;font-weight:600;display:flex;align-items:center;justify-content:center}
.socials{position:absolute;top:97px;right:18px;display:flex;gap:10px}
.socials span{width:22px;height:22px;border-radius:50%;background:#fff}
.copyright{height:55px;display:flex;align-items:center;justify-content:center;font-size:12px;color:#555}

/* mobile layout */
@media (max-width:640px){
  html,body{width:100%;height:auto;overflow:auto}
  :root{--wrap:calc(100% - 40px)}
  .site-header{height:auto}
  .site-header .wrap{flex-direction:column;padding-bottom:14px}
  .header-right{align-items:flex-start;width:100%}
  .main-nav{gap:18px;font-size:13px;flex-wrap:wrap}
  .hero{height:auto;padding:90px 20px}
  .hero-script{font-size:28px}
  .hero-title{font-size:32px;line-height:40px}
  .crumbs{flex-wrap:wrap;gap:8px;font-size:12px}
  .intro{height:auto;padding-bottom:40px}
  .intro-grid{grid-template-columns:1fr;margin-top:24px;row-gap:28px}
  .article h2{font-size:21px;line-height:30px}
  .article p{text-align:left}
  .cta{height:auto;padding:50px 0}
  .cta .wrap{width:calc(100% - 40px);flex-direction:column;align-items:flex-start;gap:30px}
  .cta-copy,.cta-art{width:100%}
  .cta-art{height:200px}
  .cta h2{font-size:30px}
  .jobs,.posts{height:auto;padding:50px 0}
  .places{height:auto;padding:50px 0}
  .sec-head{height:auto;flex-direction:column;align-items:flex-start;gap:14px}
  .sec-head h2{font-size:26px}
  .job-grid,.post-grid{grid-template-columns:1fr;padding-left:0}
  .place-row{grid-template-columns:repeat(2,1fr);padding-left:0}
  .place{height:200px}
  .place span{font-size:18px}
  .arrow{display:none}
  .footer{height:auto;padding:40px 0}
  .footer-cols{width:calc(100% - 40px);flex-wrap:wrap;gap:24px;justify-content:center}
  .footer-base{height:auto;padding:24px 20px;display:flex;flex-direction:column;gap:14px;align-items:center}
  .call,.address,.legal,.cards,.socials{position:static}
  .cards{flex-wrap:wrap;justify-content:center;gap:10px}
  .copyright{height:auto;padding:16px}
}
</style>
</head>
<body>

<header class="site-header">
  <div class="wrap">
    <a class="brand" href="#"><span class="brand-mark"></span>Brinvold Learning</a>
    <div class="header-right">
      <div class="search">
        <div class="search-field"><span>SEARCH</span><span>GO ›</span></div>
        <a class="search-btn" href="#">CHECK US ›</a>
      </div>
      <nav class="main-nav">
        <a href="#">Home</a><a href="#">Asia</a><a href="#">Teach English Online</a><a class="current" href="#">South Korea</a>
      </nav>
    </div>
  </div>
</header>

<section class="hero" role="img" aria-label="Mountain valley with green terraced fields under a cloudy sky">
  <div class="hero-script">A World of Opportunities</div>
  <h1 class="hero-title">Teach English In South Korea</h1>
  <div class="crumbs"><span>Home</span><span>›</span><span>Asia</span><span>›</span><span>Teach English online</span><span>›</span><span class="current">South Korea</span></div>
</section>

<section class="intro">
  <div class="wrap">
    <div class="meta-row">
      <div class="updated">
        <svg width="12" height="12" viewBox="0 0 12 12"><rect x="1" y="2" width="10" height="9" rx="1" fill="none" stroke="#999"/><line x1="1" y1="5" x2="11" y2="5" stroke="#999"/></svg>
        Last Updated: 27 February, 2023
      </div>
      <div class="share" aria-label="Share"><span style="background:#1877d8"></span><span style="background:#1d9bf0"></span><span style="background:#e0202a"></span></div>
    </div>
    <div class="intro-grid">
      <aside class="toc">
        <div class="toc-group"><svg width="14" height="10" viewBox="0 0 14 10"><path d="M2 2l5 5 5-5" fill="none" stroke="#14b9c1" stroke-width="2"/></svg>Introduction</div>
        <ul class="toc-sub">
          <li>Teaching experience</li>
          <li class="active">Visa requirements</li>
          <li>Certifications</li>
          <li>Degree required</li>
          <li>Non native English speaker</li>
          <li>Healthcare &amp; insurance</li>
        </ul>
        <div class="toc-group spaced"><svg width="10" height="14" viewBox="0 0 10 14"><path d="M2 2l5 5-5 5" fill="none" stroke="#14b9c1" stroke-width="2"/></svg>Requirements</div>
        <div class="toc-group spaced"><svg width="10" height="14" viewBox="0 0 10 14"><path d="M2 2l5 5-5 5" fill="none" stroke="#14b9c1" stroke-width="2"/></svg>Jobs &amp; programmes</div>
        <div class="toc-group spaced"><svg width="10" height="14" viewBox="0 0 10 14"><path d="M2 2l5 5-5 5" fill="none" stroke="#14b9c1" stroke-width="2"/></svg>Salaries &amp;benefits</div>
        <div class="toc-group spaced"><svg width="10" height="14" viewBox="0 0 10 14"><path d="M2 2l5 5-5 5" fill="none" stroke="#14b9c1" stroke-width="2"/></svg>Cost of living</div>
      </aside>
      <article class="article">
        <h2>Do you need a VISA to teach english abroad ?</h2>
        <p>Lorem ipsum dolor sit amet, consectetur adipiscing elit, sed do eiusmod tempor incididunt ut labore et dolore magna aliqua. Ut enim ad minim veniam, quis nostrud exercitation ullamco laboris nisi ut aliquip ex ea commodo consequat. Duis aute irure dolor in reprehenderit in voluptate velit esse cillum dolore eu fugiat nulla pariatur.</p>
        <p>Excepteur sint occaecat cupidatat non proident, sunt in culpa qui officia deserunt mollit anim id est laborum. Lorem ipsum dolor sit amet, consectetur adipiscing elit, sed do eiusmod tempor incididunt ut labore et dolore magna aliqua. Ut enim ad minim veniam, quis nostrud exercitation ullamco laboris nisi ut aliquip ex ea commodo consequat. Duis aute irure dolor in reprehenderit in voluptate velit esse cillum dolore eu fugiat nulla</p>
        <ul class="checks">
          <li><svg width="14" height="14" viewBox="0 0 14 14"><circle cx="7" cy="7" r="7" fill="#14b9c1"/><path d="M4 7l2 2 4-4" fill="none" stroke="#fff" stroke-width="1.6"/></svg>Nemo enim ipsam voluptatem quia voluptas</li>
          <li><svg width="14" height="14" viewBox="0 0 14 14"><circle cx="7" cy="7" r="7" fill="#14b9c1"/><path d="M4 7l2 2 4-4" fill="none" stroke="#fff" stroke-width="1.6"/></svg>Lorem ipsum dolor sit amet, consectetur</li>
          <li><svg width="14" height="14" viewBox="0 0 14 14"><circle cx="7" cy="7" r="7" fill="#14b9c1"/><path d="M4 7l2 2 4-4" fill="none" stroke="#fff" stroke-width="1.6"/></svg>Sed ut perspiciatis unde omnis</li>
          <li><svg width="14" height="14" viewBox="0 0 14 14"><circle cx="7" cy="7" r="7" fill="#14b9c1"/><path d="M4 7l2 2 4-4" fill="none" stroke="#fff" stroke-width="1.6"/></svg>Nemo enim ipsam voluptatem quia voluptas</li>
        </ul>
        <p>Ut enim ad minim veniam, quis nostrud exercitation ullamco laboris nisi ut aliquip ex ea commodo consequat. Duis aute irure dolor in reprehenderit in voluptate velit esse cillum dolore eu fugiat nulla pariatur.</p>
      </article>
    </div>
  </div>
</section>

<section class="cta">
  <div class="wrap">
    <div class="cta-copy">
      <h2>Call To Action</h2>
      <p>Lorem ipsum dolor sit amet, consectetur adipiscing elit, sed do eiusmod tempor incididunt ut labore et dolore magna aliqua. Ut enim ad minim veniam, quis nostrud exercitation</p>
      <a class="btn" href="#">Click here</a>
    </div>
    <div class="cta-art" role="img" aria-label="Paper plane flying towards an open travel factbook brochure with destination photos"></div>
  </div>
</section>

<section class="jobs">
  <div class="wrap">
    <div class="sec-head"><h2>Teaching jobs in South korea</h2><a class="btn" href="#">View All</a></div>
    <div class="job-grid">
      <div class="job"><h3>Lorem ipsum dolor sit amet, consectetur</h3><span class="badge">L</span><div class="tags"><span>SOUTH KOREA</span><span>BRINVOLD</span></div><div class="job-foot"><span>◷ Posted 2 weeks ago</span><a href="#">More info</a></div></div>
      <div class="job"><h3>Lorem ipsum dolor sit amet, consectetur</h3><span class="badge">L</span><div class="tags"><span>SOUTH KOREA</span><span>BRINVOLD</span></div><div class="job-foot"><span>◷ Posted 2 weeks ago</span><a href="#">More info</a></div></div>
      <div class="job"><h3>Lorem ipsum dolor sit amet, consectetur</h3><span class="badge">L</span><div class="tags"><span>SOUTH KOREA</span><span>BRINVOLD</span></div><div class="job-foot"><span>◷ Posted 2 weeks ago</span><a href="#">More info</a></div></div>
      <div class="job"><h3>Lorem ipsum dolor sit amet, consectetur</h3><span class="badge">L</span><div class="tags"><span>SOUTH KOREA</span><span>BRINVOLD</span></div><div class="job-foot"><span>◷ Posted 2 weeks ago</span><a href="#">More info</a></div></div>
      <div class="job"><h3>Lorem ipsum dolor sit amet, consectetur</h3><span class="badge">L</span><div class="tags"><span>SOUTH KOREA</span><span>BRINVOLD</span></div><div class="job-foot"><span>◷ Posted 2 weeks ago</span><a href="#">More info</a></div></div>
      <div class="job"><h3>Lorem ipsum dolor sit amet, consectetur</h3><span class="badge">L</span><div class="tags"><span>SOUTH KOREA</span><span>BRINVOLD</span></div><div class="job-foot"><span>◷ Posted 2 weeks ago</span><a href="#">More info</a></div></div>
    </div>
  </div>
</section>

<section class="places">
  <div class="wrap">
    <div class="sec-head"><h2>Other popular places to teach in Asia</h2><a class="btn" href="#">View All</a></div>
    <div class="place-row">
      <div class="place" role="img" aria-label="Ornate cathedral under a pink sunset sky" style="background:linear-gradient(180deg,#c97aa0,#7c4d5c 60%,#3c2b33)"><span>Duis aute irure</span></div>
      <div class="place" role="img" aria-label="Whitewashed courtyard with a small blue pool" style="background:linear-gradient(180deg,#e8dcc4,#bfa788 55%,#4f7f86)"><span>Duis aute irure</span></div>
      <div class="place" role="img" aria-label="Carved temple gable against a blue sky" style="background:linear-gradient(180deg,#6f9ccb,#3a4b66 55%,#2c2a2e)"><span>Duis aute irure</span></div>
      <div class="place" role="img" aria-label="White hillside village above the sea at dusk" style="background:linear-gradient(180deg,#e3a7a0,#c9d1dc 55%,#56606f)"><span>Duis aute irure</span></div>
    </div>
  </div>
  <a class="arrow prev" href="#" aria-label="Previous"><svg width="10" height="12" viewBox="0 0 10 12"><path d="M7 1L2 6l5 5" fill="none" stroke="#555" stroke-width="1.5"/></svg></a>
  <a class="arrow next" href="#" aria-label="Next"><svg width="10" height="12" viewBox="0 0 10 12"><path d="M3 1l5 5-5 5" fill="none" stroke="#555" stroke-width="1.5"/></svg></a>
</section>

<section class="posts">
  <div class="wrap">
    <div class="sec-head"><h2>Related Posts</h2><a class="btn" href="#">View All</a></div>
    <div class="post-grid">
      <div class="post"><div class="post-img" role="img" aria-label="Traveller resting among tropical plants" style="background:linear-gradient(160deg,#3f6e2d,#8b8a4a 60%,#5d3a24)"></div><div class="post-body"><div class="post-cat">Duis aute irure dolor</div><h3>Lorem ipsum dolor sit amet, consectetur</h3><div class="post-meta"><span><svg width="10" height="10" viewBox="0 0 10 10"><circle cx="5" cy="3" r="2.4" fill="#14b9c1"/><path d="M0.5 10a4.5 4 0 0 1 9 0z" fill="#14b9c1"/></svg>Marina Cole Hartwell</span><span><svg width="10" height="10" viewBox="0 0 10 10"><rect x=".5" y="1.5" width="9" height="8" fill="none" stroke="#14b9c1"/><line x1=".5" y1="4" x2="9.5" y2="4" stroke="#14b9c1"/></svg>Mar 13, 2023</span></div></div></div>
      <div class="post"><div class="post-img" role="img" aria-label="Person on a rock overlooking a green bay" style="background:linear-gradient(180deg,#8ab0c4,#4e7a55 55%,#6d6455)"></div><div class="post-body"><div class="post-cat">Duis aute irure dolor</div><h3>Lorem ipsum dolor sit amet, consectetur</h3><div class="post-meta"><span><svg width="10" height="10" viewBox="0 0 10 10"><circle cx="5" cy="3" r="2.4" fill="#14b9c1"/><path d="M0.5 10a4.5 4 0 0 1 9 0z" fill="#14b9c1"/></svg>Marina Cole Hartwell</span><span><svg width="10" height="10" viewBox="0 0 10 10"><rect x=".5" y="1.5" width="9" height="8" fill="none" stroke="#14b9c1"/><line x1=".5" y1="4" x2="9.5" y2="4" stroke="#14b9c1"/></svg>Mar 13, 2023</span></div></div></div>
      <div class="post"><div class="post-img" role="img" aria-label="Person wading in a rocky shallow river" style="background:linear-gradient(180deg,#b7c6cf,#6d7f86 55%,#3f4a4c)"></div><div class="post-body"><div class="post-cat">Duis aute irure dolor</div><h3>Lorem ipsum dolor sit amet, consectetur</h3><div class="post-meta"><span><svg width="10" height="10" viewBox="0 0 10 10"><circle cx="5" cy="3" r="2.4" fill="#14b9c1"/><path d="M0.5 10a4.5 4 0 0 1 9 0z" fill="#14b9c1"/></svg>Marina Cole Hartwell</span><span><svg width="10" height="10" viewBox="0 0 10 10"><rect x=".5" y="1.5" width="9" height="8" fill="none" stroke="#14b9c1"/><line x1=".5" y1="4" x2="9.5" y2="4" stroke="#14b9c1"/></svg>Mar 13, 2023</span></div></div></div>
      <div class="post"><div class="post-img" role="img" aria-label="Traveller sitting in a boat on a green lake" style="background:linear-gradient(160deg,#b6c23e,#6f8a2a 55%,#3d5220)"></div><div class="post-body"><div class="post-cat">Duis aute irure dolor</div><h3>Lorem ipsum dolor sit amet, consectetur</h3><div class="post-meta"><span><svg width="10" height="10" viewBox="0 0 10 10"><circle cx="5" cy="3" r="2.4" fill="#14b9c1"/><path d="M0.5 10a4.5 4 0 0 1 9 0z" fill="#14b9c1"/></svg>Marina Cole Hartwell</span><span><svg width="10" height="10" viewBox="0 0 10 10"><rect x=".5" y="1.5" width="9" height="8" fill="none" stroke="#14b9c1"/><line x1=".5" y1="4" x2="9.5" y2="4" stroke="#14b9c1"/></svg>Mar 13, 2023</span></div></div></div>
      <div class="post"><div class="post-img" role="img" aria-label="City skyline across a blue harbour and hills" style="background:linear-gradient(180deg,#c5d6e2,#5e8aa6 50%,#2f5a4a)"></div><div class="post-body"><div class="post-cat">Duis aute irure dolor</div><h3>Lorem ipsum dolor sit amet, consectetur</h3><div class="post-meta"><span><svg width="10" height="10" viewBox="0 0 10 10"><circle cx="5" cy="3" r="2.4" fill="#14b9c1"/><path d="M0.5 10a4.5 4 0 0 1 9 0z" fill="#14b9c1"/></svg>Marina Cole Hartwell</span><span><svg width="10" height="10" viewBox="0 0 10 10"><rect x=".5" y="1.5" width="9" height="8" fill="none" stroke="#14b9c1"/><line x1=".5" y1="4" x2="9.5" y2="4" stroke="#14b9c1"/></svg>Mar 13, 2023</span></div></div></div>
      <div class="post"><div class="post-img" role="img" aria-label="Hiker with a backpack on a green tea hillside" style="background:linear-gradient(180deg,#8fb069,#4d7a35 55%,#2f4e24)"></div><div class="post-body"><div class="post-cat">Duis aute irure dolor</div><h3>Lorem ipsum dolor sit amet, consectetur</h3><div class="post-meta"><span><svg width="10" height="10" viewBox="0 0 10 10"><circle cx="5" cy="3" r="2.4" fill="#14b9c1"/><path d="M0.5 10a4.5 4 0 0 1 9 0z" fill="#14b9c1"/></svg>Marina Cole Hartwell</span><span><svg width="10" height="10" viewBox="0 0 10 10"><rect x=".5" y="1.5" width="9" height="8" fill="none" stroke="#14b9c1"/><line x1=".5" y1="4" x2="9.5" y2="4" stroke="#14b9c1"/></svg>Mar 13, 2023</span></div></div></div>
    </div>
  </div>
</section>

<footer>
  <div class="footer">
    <div class="footer-brand"><i></i>Brinvold Learning</div>
    <div class="footer-cols">
      <div class="footer-col"><h4>Why Brinvold?</h4><ul><li>Why Choose Us?</li><li>Charity Partnership</li><li>Accreditation</li><li>Compare Course Providers</li><li>Meet our Alumni</li><li>Meet our Trainers</li><li>Company profile</li><li>Testimonials</li><li>Affiliate Programme</li></ul></div>
      <div class="footer-col"><h4>TEFL Courses</h4><ul><li>View All TEFL Courses</li><li>Online TEFL Course (Level 3 – 120hrs)</li><li>Online TEFL Course (Level 5 – 168hrs)</li><li>Observed Teaching Practice Course (Level 5)</li><li>TEFL Top-Up Courses</li></ul></div>
      <div class="footer-col"><h4>Teaching Opportunities</h4><ul><li>TEFL Jobs</li><li>TEFL Internships</li><li>TEFL Volunteering</li><li>Country Profiles</li><li>Teaching without a Degree</li></ul></div>
      <div class="footer-col"><h4>Student Support Centre</h4><ul><li>TEFL Learning Centre</li><li>Frequently Asked Questions</li></ul></div>
      <div class="footer-col"><h4>Talk to Us</h4><ul><li>Get in Touch</li><li>Request Call Back</li><li>Blog</li></ul></div>
    </div>
  </div>
  <div class="footer-base" role="img" aria-label="Dark tropical palm trees at dusk">
    <div class="call">Call us for help +1 555 014 7730</div>
    <div class="cards"><span>Card</span><span>Debit</span><span>Bank</span><span>Credit</span><span>Prepay</span><span>Wallet</span></div>
    <div class="address">Brinvold Learning, 218 Harlow Street, #52 Millbrook, NY 10990, USA</div>
    <div class="legal">Terms and Conditions &nbsp;|&nbsp; Privacy Policy</div>
    <div class="socials"><span></span><span></span><span></span><span></span><span></span></div>
  </div>
  <div class="copyright">© Copyrights 2023 Company Name | All Rights reserved</div>
</footer>

</body>
</html>
```